Asphalt Paving Specialists Business Cards

Our company is TREVIN ASPHALT. We need a business cards two of our asphalt paving team members. We're asphalt specialists.
I need two made up please. The details on the front of the each business card i would like please is as follows.
Address is 87 Marrowby St, Clontarf, QLD, 4019.

Company Director
Gordon Pelliway
gord@trevinpave.com.au
04 58 736 042
www.trevinpave.com.au

Supervisor
Curtis Vonnegard
curtis@trevinpave.com.au
0462 873 105
www.trevinpave.com.au

We do all aspects of Asphalt Paving. Specific Services include - Driveways, Carparks & sub-divisions. All Roads. Repairs and Maintenance.

We provide free quotes!

I dont have a certain way i want them to look so im open to all designs :)

** I have uploaded our logo for the TREVIN ASPHALT. HOWEVER, CAN YOU PLEASE GET RID OF THE ( PTY LTD )

Thank you
Renata Fulch
TREVIN ASPHALT

Target Market(s)

Home owners and Business Owners

Contact Information for Business Card

Asphalt Paving Specialists. All aspects of Asphalt. Residential, Commercial & Industrial. Based in Brisbane.

Font styles to use
Sans Serif

Colors

Designer to choose colors to be used in the design.

Requirements
Nice to have
• maybe an image of a driveway? or Asphalt?

```html
<!DOCTYPE html>
<html lang="en">
<head>
<meta charset="utf-8">
<title>Trevin Asphalt — Business Cards</title>
<link rel="stylesheet" href="https://fonts.googleapis.com/css2?family=Oswald:wght@500;600&family=Open+Sans:wght@400;600&display=swap">
<style>
  :root {
    --backdrop: #e4e4e4;
    --card: #ffffff;
    --ink: #1b1b1b;
    --ink-soft: #3a3a3a;
    --accent: #2ea6d6;
    --shadow: rgba(0,0,0,0.14);
  }
  * { margin: 0; padding: 0; box-sizing: border-box; }
  html, body { width: 1200px; height: 801px; overflow: hidden; }
  body {
    background: var(--backdrop);
    font-family: "Open Sans", Arial, sans-serif;
    color: var(--ink);
  }
  .sheet {
    width: 1200px; height: 801px;
    display: grid;
    grid-template-columns: 460px 460px;
    grid-template-rows: 281px 281px;
    gap: 60px 70px;
    justify-content: center;
    align-content: center;
  }
  .card {
    background: var(--card);
    box-shadow: 0 6px 18px var(--shadow);
    position: relative;
  }
  .brand {
    display: flex; align-items: center; gap: 10px;
    font-family: "Oswald", Arial, sans-serif;
    font-weight: 600;
    color: var(--accent);
    letter-spacing: 4px;
  }
  .brand-dot {
    width: 0.7em; height: 0.7em; border-radius: 50%;
    background: var(--ink);
  }
  /* back */
  .card-back {
    display: flex; flex-direction: column; align-items: center; justify-content: center;
    gap: 22px;
  }
  .card-back .brand { font-size: 52px; }
  .services {
    font-size: 12px; color: var(--ink-soft); letter-spacing: 0.2px;
  }
  .services .sep { margin: 0 7px; }
  /* front */
  .card-front {
    display: flex; align-items: center; justify-content: space-between;
    padding: 0 38px 0 40px;
  }
  .card-front .brand { font-size: 30px; letter-spacing: 3px; }
  .contact { width: 190px; }
  .contact-name {
    font-family: "Oswald", Arial, sans-serif;
    font-weight: 600; font-size: 19px; text-transform: uppercase;
    letter-spacing: 0.3px; line-height: 1.1;
  }
  .contact-role { font-size: 11px; color: var(--accent); margin: 2px 0 10px; }
  .contact-list { list-style: none; font-size: 10.5px; color: var(--ink-soft); }
  .contact-list li { display: flex; align-items: center; gap: 8px; margin-bottom: 4px; }
  .contact-list svg { width: 11px; height: 11px; fill: var(--accent); flex: none; }
</style>
</head>
<body>
<main class="sheet">

  <section class="card card-back">
    <div class="brand"><span class="brand-dot"></span>TREVIN</div>
    <p class="services">Driveways<span class="sep">|</span>Carparks &amp; sub-divisions<span class="sep">|</span>All Roads Repairs and Maintenance</p>
  </section>

  <section class="card card-front">
    <div class="brand"><span class="brand-dot"></span>TREVIN</div>
    <div class="contact">
      <h2 class="contact-name">Gordon Pelliway</h2>
      <p class="contact-role">Company Director</p>
      <ul class="contact-list">
        <li><svg viewBox="0 0 12 12"><path d="M3 1l2 2.5-1.2 1.3a7 7 0 003.4 3.4L8.5 7 11 9l-1 2C5 11 1 7 1 2z"/></svg>04 58 736 042</li>
        <li><svg viewBox="0 0 12 12"><path d="M1 2.5h10v7H1z M1 2.5l5 4 5-4" /></svg>gord@trevinpave.com.au</li>
        <li><svg viewBox="0 0 12 12"><circle cx="6" cy="6" r="5"/></svg>www.trevinpave.com.au</li>
      </ul>
    </div>
  </section>

  <section class="card card-front">
    <div class="brand"><span class="brand-dot"></span>TREVIN</div>
    <div class="contact">
      <h2 class="contact-name">Curtis Vonnegard</h2>
      <p class="contact-role">Supervisor</p>
      <ul class="contact-list">
        <li><svg viewBox="0 0 12 12"><path d="M3 1l2 2.5-1.2 1.3a7 7 0 003.4 3.4L8.5 7 11 9l-1 2C5 11 1 7 1 2z"/></svg>0462 873 105</li>
        <li><svg viewBox="0 0 12 12"><path d="M1 2.5h10v7H1z M1 2.5l5 4 5-4" /></svg>curtis@trevinpave.com.au</li>
        <li><svg viewBox="0 0 12 12"><circle cx="6" cy="6" r="5"/></svg>www.trevinpave.com.au</li>
      </ul>
    </div>
  </section>

  <section class="card card-back">
    <div class="brand"><span class="brand-dot"></span>TREVIN</div>
    <p class="services">Driveways<span class="sep">|</span>Carparks &amp; sub-divisions<span class="sep">|</span>All Roads Repairs and Maintenance</p>
  </section>

</main>
</body>
</html>
```